Brand new website for global research and investment startup

We need a simple website, maybe 3 pages: landing page with business description, investment philosophy, team and contact info.
We have a logo already that can be incorporated. Please use the logo only, not the text
We like the color green, something along the lines of #3D6C32 as the main color.
We'd like to design the website with geometric shapes in gradations of the base color. The shapes should suggest "work in progress", "built to last (a long time)", "solidity" and "indestructibility". One idea floating in my head sees smaller features with icosahedron and dodecahedron shapes, and maybe larger structures like crystal lattices; but please feel free to be creative and imagine your own.

```html
<!DOCTYPE html>
<html lang="en">
<head>
<meta charset="utf-8">
<title>Insights — Stratum Partners</title>
<link href="https://fonts.googleapis.com/css2?family=Inter:wght@400;500;600;700&display=swap" rel="stylesheet">
<style>
:root{
  --green-900:#2c5a2f;
  --green-800:#33613a;
  --green-700:#3d6c32;
  --green-500:#4a9a3f;
  --green-400:#52a844;
  --ink:#2d5a2e;
  --text:#6f7a72;
  --muted:#8b948d;
  --bg-soft:#f6f8f6;
  --line:#e6ebe6;
  --white:#ffffff;
}
*{box-sizing:border-box;margin:0;padding:0}
html,body{width:1200px;height:2850px;overflow:hidden}
body{font-family:"Inter",sans-serif;color:var(--ink);background:var(--white)}
.wrap{width:1010px;margin-left:95px}
a{color:inherit;text-decoration:none}

.site-header{height:82px;display:flex;align-items:center;background:var(--white);box-shadow:0 2px 8px rgba(0,0,0,.04);position:relative;z-index:2}
.site-header .wrap{display:flex;justify-content:space-between;align-items:center}
.brand{font-weight:700;font-size:22px;color:var(--green-700);display:flex;align-items:center;gap:10px}
.brand-mark{width:14px;height:14px;background:var(--green-700)}
.main-nav{display:flex;gap:36px;font-size:14px;font-weight:500}
.main-nav a{padding-bottom:6px;border-bottom:2px solid transparent}
.main-nav a.active{border-bottom-color:var(--green-400)}

.hero{height:310px;background:linear-gradient(180deg,#f7f9f7,#fff);position:relative;padding-top:61px}
.hero::after{content:"";position:absolute;left:0;right:0;bottom:0;height:2px;background:linear-gradient(90deg,transparent,var(--green-400),transparent)}
.pill{display:inline-block;font-size:12.5px;font-weight:500;padding:9px 14px;border-radius:20px;background:#e8f0e6;border:1px solid #cfdccc;color:var(--ink)}
.hero h1{font-size:60px;font-weight:600;letter-spacing:-1px;margin-top:22px;color:var(--green-800)}
.hero h1 span{color:var(--green-500)}
.hero p{font-size:17.5px;line-height:28px;color:var(--muted);margin-top:16px;width:540px}

.featured-section{height:555px;padding-top:87px}
.featured-card{display:flex;height:381px;border:1px solid var(--line);border-radius:12px;overflow:hidden;box-shadow:0 6px 20px rgba(0,0,0,.04)}
.featured-media{width:505px;background:linear-gradient(135deg,#2f6434,#52a844);position:relative;display:flex;align-items:center;justify-content:center}
.tag{position:absolute;top:14px;left:14px;background:var(--white);color:var(--ink);font-size:11px;font-weight:500;padding:6px 10px;border-radius:14px}
.featured-body{padding:45px 42px 0}
.date{font-size:12.5px;color:var(--muted)}
.featured-body h2{font-size:25px;font-weight:600;line-height:29px;margin-top:13px;color:var(--green-800)}
.featured-body p{font-size:13.6px;line-height:21.6px;color:var(--text);margin-top:18px}
.read{display:inline-flex;align-items:center;gap:8px;font-weight:600;font-size:14.5px;margin-top:24px;color:var(--green-800)}

.all-insights{height:1097px;background:var(--bg-soft);padding-top:88px}
.all-insights h2{font-size:44px;font-weight:600;color:var(--green-800)}
.grid{display:grid;grid-template-columns:repeat(3,316px);gap:31px 30px;margin-top:44px}
.card{height:400px;background:var(--white);border-radius:10px;overflow:hidden;box-shadow:0 4px 14px rgba(0,0,0,.05)}
.card-media{height:178px;position:relative;display:flex;align-items:center;justify-content:center}
.g1{background:linear-gradient(135deg,#2f6035,#3a7a36)}
.g2{background:linear-gradient(135deg,#52a844,#3a7a36 70%,#2f6035)}
.g3{background:linear-gradient(135deg,#2f6035,#52a844)}
.card-body{padding:24px 22px 0}
.card-body h3{font-size:18px;font-weight:600;line-height:20.5px;margin-top:11px;color:var(--green-800)}
.card-body p{font-size:13.6px;line-height:21.6px;color:var(--text);margin-top:12px}
.card .read{font-size:13px;margin-top:18px}

.newsletter{height:359px;background:linear-gradient(135deg,#2f5e35,#3f7436);color:var(--white);text-align:center;padding-top:86px}
.newsletter h2{font-size:44px;font-weight:600}
.newsletter p{font-size:15.5px;line-height:24px;width:420px;margin:18px auto 0;opacity:.95}
.subscribe-form{display:flex;justify-content:center;gap:14px;margin-top:30px}
.subscribe-form input{width:303px;height:46px;border-radius:23px;border:none;padding:0 21px;font:14.5px "Inter",sans-serif;color:var(--text)}
.subscribe-form button{height:46px;padding:0 28px;border-radius:23px;border:none;background:var(--white);color:var(--green-800);font:600 16px Georgia,serif}

.disclaimer{height:97px;display:flex;align-items:center}
.disclaimer .wrap{display:flex;gap:14px;align-items:center}
.shield{width:36px;height:36px;border-radius:50%;background:#eef3ed;display:flex;align-items:center;justify-content:center;flex:none}
.disclaimer p{font-size:11.8px;line-height:19.5px;color:var(--muted);width:920px}

.site-footer{height:350px;background:var(--green-900);border-top:4px solid var(--green-400);color:#e4ede3;padding-top:52px}
.footer-top{display:flex}
.footer-brand{width:393px}
.footer-brand .brand{color:var(--white);font-size:22px}
.footer-brand .brand-mark{background:var(--white)}
.footer-brand p{font-size:14px;line-height:22px;margin-top:14px;width:290px}
.footer-col{width:218px}
.footer-col:last-child{width:auto}
.footer-col h4{font-size:14.5px;font-weight:600;color:var(--white)}
.footer-col ul{list-style:none;margin-top:24px}
.footer-col li{font-size:13.3px;line-height:30.5px}
.footer-bottom{display:flex;justify-content:space-between;align-items:center;margin-top:62px;border-top:1px solid rgba(255,255,255,.12);padding-top:22px;font-size:12px}
.socials{display:flex;gap:14px}
.socials span{width:36px;height:36px;border-radius:50%;background:rgba(255,255,255,.12);display:block}
</style>
</head>
<body>
<header class="site-header">
  <div class="wrap">
    <a class="brand" href="#"><span class="brand-mark"></span>Stratum Partners</a>
    <nav class="main-nav">
      <a href="#">Home</a><a href="#">Philosophy</a><a class="active" href="#">Insights</a><a class="active" href="#">Team &amp; Contact</a>
    </nav>
  </div>
</header>

<section class="hero">
  <div class="wrap">
    <span class="pill">Research &amp; Analysis</span>
    <h1>Latest <span>Insights</span></h1>
    <p>Research-driven perspectives on markets, investment strategy, and the businesses we partner with.</p>
  </div>
</section>

<section class="featured-section">
  <div class="wrap">
    <article class="featured-card">
      <div class="featured-media" role="img" aria-label="Featured article visual in green tones">
        <span class="tag">Featured</span>
        <svg width="66" height="60" viewBox="0 0 24 24" fill="none" stroke="rgba(255,255,255,.35)" stroke-width="1.4" stroke-linecap="round" stroke-linejoin="round"><path d="M2 12h4l3-8 6 16 3-8h4"/></svg>
      </div>
      <div class="featured-body">
        <div class="date">August 15, 2026</div>
        <h2>Navigating Volatility: A Long-Term Perspective on European Markets</h2>
        <p>In periods of market uncertainty, the temptation to react emotionally can be overwhelming. However, our analysis of market cycles over the past two decades reveals that short-term volatility often creates the most compelling opportunities for disciplined, long-term investors. This paper examines current market dynamics and why we believe maintaining conviction in quality businesses remains the optimal strategy.</p>
        <a class="read" href="#">Read Full Article <svg width="12" height="12" viewBox="0 0 24 24" fill="none" stroke="currentColor" stroke-width="2.5"><path d="M4 12h15M13 6l6 6-6 6"/></svg></a>
      </div>
    </article>
  </div>
</section>

<section class="all-insights">
  <div class="wrap">
    <h2>All Insights</h2>
    <div class="grid">
      <article class="card">
        <div class="card-media g1"><span class="tag">Investment Strategy</span>
          <svg width="48" height="48" viewBox="0 0 24 24" fill="none" stroke="rgba(255,255,255,.3)" stroke-width="1.4"><rect x="3" y="3" width="7" height="7"/><rect x="14" y="3" width="7" height="7"/><rect x="3" y="14" width="7" height="7"/><rect x="14" y="14" width="7" height="7"/></svg></div>
        <div class="card-body"><div class="date">August 8, 2026</div><h3>The Power of Conviction-Sizing</h3><p>How concentrated positions in high-conviction ideas can enhance portfolio returns while managing overall risk.</p><a class="read" href="#">Read More <svg width="11" height="11" viewBox="0 0 24 24" fill="none" stroke="currentColor" stroke-width="2.5"><path d="M4 12h15M13 6l6 6-6 6"/></svg></a></div>
      </article>
      <article class="card">
        <div class="card-media g2"><span class="tag">Sector Research</span>
          <svg width="52" height="52" viewBox="0 0 24 24" fill="none" stroke="rgba(255,255,255,.3)" stroke-width="1.4"><circle cx="12" cy="12" r="9"/><path d="M12 7v5l3 2"/></svg></div>
        <div class="card-body"><div class="date">July 29, 2026</div><h3>Emerging Opportunities in European Tech</h3><p>Identifying undervalued innovation hubs across the European technology landscape and their growth potential.</p><a class="read" href="#">Read More <svg width="11" height="11" viewBox="0 0 24 24" fill="none" stroke="currentColor" stroke-width="2.5"><path d="M4 12h15M13 6l6 6-6 6"/></svg></a></div>
      </article>
      <article class="card">
        <div class="card-media g3"><span class="tag">Regulation</span>
          <svg width="50" height="50" viewBox="0 0 24 24" fill="none" stroke="rgba(255,255,255,.3)" stroke-width="1.4"><path d="M12 3l7 3v6c0 4-3 7-7 9-4-2-7-5-7-9V6z"/></svg></div>
        <div class="card-body"><div class="date">July 15, 2026</div><h3>UCITS Framework: Investor Protection</h3><p>Understanding how UCITS compliance provides structural advantages and safeguards for institutional investors.</p><a class="read" href="#">Read More <svg width="11" height="11" viewBox="0 0 24 24" fill="none" stroke="currentColor" stroke-width="2.5"><path d="M4 12h15M13 6l6 6-6 6"/></svg></a></div>
      </article>
      <article class="card">
        <div class="card-media g1"><span class="tag">Market Analysis</span>
          <svg width="48" height="48" viewBox="0 0 24 24" fill="none" stroke="rgba(255,255,255,.3)" stroke-width="1.4"><path d="M6 20v-4M12 20v-8M18 20V4"/></svg></div>
        <div class="card-body"><div class="date">July 1, 2026</div><h3>Valuation Discipline in Growth Markets</h3><p>Why maintaining valuation sensitivity remains crucial even when growth opportunities appear compelling.</p><a class="read" href="#">Read More <svg width="11" height="11" viewBox="0 0 24 24" fill="none" stroke="currentColor" stroke-width="2.5"><path d="M4 12h15M13 6l6 6-6 6"/></svg></a></div>
      </article>
      <article class="card">
        <div class="card-media g2"><span class="tag">Partnership</span>
          <svg width="56" height="52" viewBox="0 0 24 24" fill="none" stroke="rgba(255,255,255,.3)" stroke-width="1.4"><circle cx="9" cy="8" r="3.5"/><path d="M2 20c0-4 3-6 7-6s7 2 7 6M16 4.5a3.5 3.5 0 0 1 0 7M19 14c2 .8 3 2.8 3 6"/></svg></div>
        <div class="card-body"><div class="date">June 18, 2026</div><h3>Building Lasting Founder Relationships</h3><p>How partnership-driven investing creates mutual value for investors and the entrepreneurs they support.</p><a class="read" href="#">Read More <svg width="11" height="11" viewBox="0 0 24 24" fill="none" stroke="currentColor" stroke-width="2.5"><path d="M4 12h15M13 6l6 6-6 6"/></svg></a></div>
      </article>
      <article class="card">
        <div class="card-media g3"><span class="tag">Quarterly Review</span>
          <svg width="52" height="48" viewBox="0 0 24 24" fill="none" stroke="rgba(255,255,255,.3)" stroke-width="1.4" stroke-linejoin="round"><path d="M2 12h4l3-8 6 16 3-8h4"/></svg></div>
        <div class="card-body"><div class="date">June 5, 2026</div><h3>Q2 2026 Market Commentary</h3><p>Our assessment of portfolio performance, market conditions, and strategic positioning for the quarters ahead.</p><a class="read" href="#">Read More <svg width="11" height="11" viewBox="0 0 24 24" fill="none" stroke="currentColor" stroke-width="2.5"><path d="M4 12h15M13 6l6 6-6 6"/></svg></a></div>
      </article>
    </div>
  </div>
</section>

<section class="newsletter">
  <h2>Stay Informed</h2>
  <p>Receive our latest insights and research directly. Available exclusively to professional investors.</p>
  <form class="subscribe-form"><input type="email" placeholder="Enter your email"><button type="button">Subscribe</button></form>
</section>

<section class="disclaimer">
  <div class="wrap">
    <span class="shield"><svg width="16" height="16" viewBox="0 0 24 24" fill="none" stroke="#3d6c32" stroke-width="2"><path d="M12 3l7 3v6c0 4-3 7-7 9-4-2-7-5-7-9V6z"/></svg></span>
    <p>This website is intended for professional investors only. All investment strategies involve risk of loss. Past performance is not indicative of future results. UCITS compliant funds are subject to regulatory requirements.</p>
  </div>
</section>

<footer class="site-footer">
  <div class="wrap">
    <div class="footer-top">
      <div class="footer-brand">
        <div class="brand"><span class="brand-mark"></span>Stratum Partners</div>
        <p>Disciplined equity research and investment partnerships for professional investors.</p>
      </div>
      <div class="footer-col"><h4>Navigation</h4><ul><li>Home</li><li>Philosophy</li><li>Insights</li><li>Team &amp; Contact</li></ul></div>
      <div class="footer-col"><h4>Approach</h4><ul><li>Investment Process</li><li>Conviction Sizing</li><li>Sector Diversification</li><li>UCITS Compliance</li></ul></div>
      <div class="footer-col"><h4>Contact</h4><ul><li>hello@stratumpartners.example</li><li>+41 22 555 01 90</li><li>Zurich, Switzerland</li></ul></div>
    </div>
    <div class="footer-bottom">
      <span>© 2026 Stratum Partners. All rights reserved.</span>
      <div class="socials"><span aria-label="Professional network"></span><span aria-label="Social feed"></span></div>
    </div>
  </div>
</footer>
</body>
</html>
```